Cover Art for my Podcast- Tides, Lanterns and a Slice of Toast

I'm both a life coach and a death doula looking to give both life advice and educate people on how to have a better death, whether planning for the future or if they're facing dying in the short term

Requirements
Must have
• Must be square, 3000px x 3000px max

```html
<!DOCTYPE html>
<html lang="en">
<head>
<meta charset="utf-8">
<title>Tides, Lanterns and a Slice of Toast — Podcast Cover</title>
<link href="https://fonts.googleapis.com/css2?family=Oswald:wght@700&family=Poppins:wght@600&display=swap" rel="stylesheet">
<style>
  :root {
    --moss: #9aa73a;
    --moss-dark: #8a9830;
    --night: #0e0e0e;
    --night-soft: #262626;
    --ash: #98989c;
    --chalk: #ffffff;
    --saucer: #f2f2f2;
    --saucer-shade: #cfcfcf;
    --brew: #1a0806;
  }
  html, body {
    margin: 0;
    padding: 0;
    width: 1200px;
    height: 1200px;
    overflow: hidden;
    background: var(--night);
  }
  .cover {
    position: relative;
    width: 1200px;
    height: 1200px;
  }
  .cover svg { display: block; }
  .title-line {
    font-family: "Oswald", "Arial Narrow", sans-serif;
    font-weight: 700;
  }
  .title-line--first { fill: var(--moss); font-size: 250px; }
  .title-line--second { fill: var(--ash); font-size: 168px; }
  .title-line--third { fill: var(--chalk); font-size: 112px; }
  .badge-label {
    font-family: "Poppins", "Helvetica", sans-serif;
    font-weight: 600;
    font-size: 38px;
    letter-spacing: 8px;
    fill: var(--chalk);
  }
</style>
</head>
<body>
<div class="cover">
  <svg width="1200" height="1200" viewBox="0 0 1200 1200" xmlns="http://www.w3.org/2000/svg">
    <defs>
      <linearGradient id="moss-band" x1="0" y1="0" x2="1" y2="1">
        <stop offset="0" stop-color="#a2ae42"/>
        <stop offset="1" stop-color="var(--moss-dark)"/>
      </linearGradient>
      <radialGradient id="night-field" cx="0.4" cy="0.45" r="0.7">
        <stop offset="0" stop-color="var(--night-soft)"/>
        <stop offset="1" stop-color="var(--night)"/>
      </radialGradient>
      <radialGradient id="cup-photo" cx="0.5" cy="0.5" r="0.5">
        <stop offset="0" stop-color="var(--brew)"/>
        <stop offset="0.55" stop-color="#3a1a0c"/>
        <stop offset="0.6" stop-color="#ffffff"/>
        <stop offset="0.9" stop-color="var(--saucer)"/>
        <stop offset="1" stop-color="var(--saucer-shade)"/>
      </radialGradient>
    </defs>

    <!-- dark field -->
    <rect class="field" x="0" y="0" width="1200" height="1200" fill="url(#night-field)"/>

    <!-- green band -->
    <rect class="band" x="0" y="0" width="1200" height="257" fill="url(#moss-band)"/>

    <!-- heartbeat cut into the band -->
    <polygon class="pulse-fill"
      points="171,257 187,212 240,338 312,75 391,391 441,198 482,314 500,257"
      fill="var(--night)"/>
    <polyline class="pulse-line"
      points="0,257 171,257 187,212 240,338 312,75 391,391 441,198 482,314 500,257 1200,257"
      fill="none" stroke="var(--chalk)" stroke-width="10" stroke-linejoin="round" stroke-linecap="round"/>

    <!-- podcast badge -->
    <g class="podcast-badge">
      <path d="M823,86 H1200 V171 H823 A42.5,42.5 0 0 1 823,86 Z" fill="#000"/>
      <g class="mic-icon" fill="none" stroke="var(--moss)" stroke-width="2.5" stroke-linecap="round">
        <path d="M830,112 a18,18 0 0 0 0,26"/>
        <path d="M824,106 a26,26 0 0 0 0,38"/>
        <path d="M872,112 a18,18 0 0 1 0,26"/>
        <path d="M878,106 a26,26 0 0 1 0,38"/>
        <path d="M840,130 a11,11 0 0 0 22,0"/>
        <line x1="851" y1="141" x2="851" y2="158"/>
        <line x1="845" y1="158" x2="857" y2="158"/>
      </g>
      <rect x="843" y="104" width="16" height="32" rx="8" fill="var(--chalk)"/>
      <text class="badge-label" x="892" y="143">PODCAST</text>
    </g>

    <!-- cup photograph area -->
    <circle class="cup-photo" cx="887" cy="692" r="266" fill="url(#cup-photo)"
      role="img" aria-label="Top-down photo of a white cup of black coffee on a saucer"/>

    <!-- title -->
    <text class="title-line title-line--first" x="46" y="687">Tides,</text>
    <text class="title-line title-line--second" x="46" y="951">Lanterns</text>
    <text class="title-line title-line--third" x="46" y="1144">and a Slice of Toast</text>
  </svg>
</div>
</body>
</html>
```